Hadley's Groundwork Crew needs a logo/business cards.

i've just started a new Labouring Business, Called Hadley's Groundwork Crew, I provide high quality labouring servicing to local Builders and Tradesmen.
I'd like my business cards to reflect the hard work and dedication I put into my business.
I'd like to see Burnt Orange and blacks in the cards and logo.
I want my cards to catch peoples eye as there is A lot of dull business cards in my industry.

Target Market(s)

Builders and other tradesmen

Contact Information for Business Card

Hadley's Groundwork Crew

Font styles to use
Sans Serif

Colors
f78f20
ffc214
000000
ffffff

Requirements
Must have
• My name : Tom Hadley
• My Number: 0457962381
• Email Address : hadleygroundworkcrew@mailbarn.net
• A Sharp and Professional Design
Nice to have
• A unique design that separates my Cards from others,
• As I try to provide unique service to my clients I'd love my cards/logo to reflect this.

```html
<!DOCTYPE html>
<html lang="en">
<head>
<meta charset="utf-8">
<title>Hadley's Groundwork Crew — Business Cards</title>
<link rel="stylesheet" href="https://fonts.googleapis.com/css2?family=Exo+2:wght@500;600&family=Arimo:wght@400&display=swap">
<style>
  :root {
    --stage: #141517;
    --card: #222427;
    --yellow: #ffc214;
    --orange: #f78f20;
    --white: #ffffff;
    --muted: #e6e6e6;
  }
  * { box-sizing: border-box; margin: 0; padding: 0; }
  html, body { width: 1200px; height: 800px; overflow: hidden; background: var(--stage); }
  .stage {
    width: 1200px; height: 800px;
    display: flex; align-items: center; justify-content: center; gap: 40px;
  }
  .card {
    width: 540px; height: 310px;
    background: var(--card);
    border-radius: 18px;
    position: relative;
    box-shadow: 0 18px 40px rgba(0,0,0,.55);
    font-family: "Exo 2", sans-serif;
    overflow: hidden;
  }

  /* Front */
  .card--front { display: flex; align-items: center; justify-content: center; }
  .brand { display: flex; align-items: center; gap: 22px; }
  .brand__dot { width: 64px; height: 64px; border-radius: 50%; background: var(--orange); flex: none; }
  .brand__name {
    color: var(--yellow); font-weight: 600; font-size: 38px; line-height: 1.08;
    letter-spacing: .5px; width: 260px;
  }

  /* Back */
  .mark {
    position: absolute; left: 32px; top: 0; bottom: 0; width: 196px;
    display: flex; flex-direction: column; justify-content: center; gap: 12px;
  }
  .mark__square { width: 30px; height: 30px; background: var(--orange); }
  .mark__name { color: var(--white); font-weight: 600; font-size: 30px; line-height: 1.08; }

  .details { position: absolute; left: 248px; top: 44px; right: 22px; }
  .details__company { color: var(--yellow); font-weight: 500; font-size: 42px; letter-spacing: 2px; line-height: 1; }
  .details__tagline { color: var(--white); font-weight: 500; font-size: 20px; letter-spacing: .5px; margin-top: 4px; }
  .details__rule { height: 2px; background: var(--orange); margin: 16px 0 14px; width: 250px; }
  .details__person { color: var(--white); font-weight: 500; font-size: 21px; letter-spacing: .5px; line-height: 1.1; }
  .details__role { color: var(--orange); font-weight: 500; font-size: 14px; margin-top: 2px; }
  .contact { list-style: none; margin-top: 22px; display: flex; flex-direction: column; gap: 9px; }
  .contact__item { display: flex; align-items: center; gap: 10px; color: var(--muted); font-family: "Arimo", sans-serif; font-size: 13.5px; white-space: nowrap; }
  .contact__icon { width: 13px; height: 13px; flex: none; }
</style>
</head>
<body>
<main class="stage">
  <section class="card card--front" aria-label="Business card front">
    <div class="brand">
      <span class="brand__dot"></span>
      <span class="brand__name">Hadley's Groundwork Crew</span>
    </div>
  </section>

  <section class="card card--back" aria-label="Business card back">
    <div class="mark">
      <span class="mark__square"></span>
      <span class="mark__name">Hadley's Groundwork Crew</span>
    </div>
    <div class="details">
      <p class="details__company">Hadley's</p>
      <p class="details__tagline">Groundwork Crew</p>
      <div class="details__rule"></div>
      <p class="details__person">Tom Hadley</p>
      <p class="details__role">Manager</p>
      <ul class="contact">
        <li class="contact__item">
          <svg class="contact__icon" viewBox="0 0 14 14" aria-hidden="true"><rect x="2" y="1" width="10" height="12" rx="1.5" fill="none" stroke="#ffc214" stroke-width="1.8"/></svg>
          0457962381
        </li>
        <li class="contact__item">
          <svg class="contact__icon" viewBox="0 0 14 14" aria-hidden="true"><rect x="1" y="3" width="12" height="8" fill="#ffc214"/><path d="M1 3 L7 8 L13 3" fill="none" stroke="#222427" stroke-width="1.2"/></svg>
          hadleygroundworkcrew@mailbarn.net
        </li>
      </ul>
    </div>
  </section>
</main>
</body>
</html>
```